Modern Lawfirm Business Card Design

We're looking for a business card to incorporate the newly created logo we had made.

Ideally looking for a law firm business card demonstrating, modern, minimalist, strong/bold design.

I'm open to any design honestly, but nothing "flashy".

Target Market(s)

Immigration law, family immigration, humanitarian, general legal

Industry/Entity Type

Law Firm

Contact Information for Business Card

Please use dummy information, name, street address, city, state, phone number, email, website.

Font styles to use
Serif
Sans Serif

Requirements
Must have
• Please use dummy information, name, street address, city, state, phone number, email, website.

```html
<!DOCTYPE html>
<html lang="en">
<head>
<meta charset="utf-8">
<title>Valdera Immigration Law – Business Card</title>
<link href="https://fonts.googleapis.com/css2?family=Arimo:wght@400&display=swap" rel="stylesheet">
<style>
  :root {
    --navy: #114a87;
    --ink: #1c1c1c;
    --paper: #ffffff;
    --edge: #c8c8c8;
  }
  * { margin: 0; padding: 0; box-sizing: border-box; }
  html, body {
    width: 1200px;
    height: 960px;
    overflow: hidden;
    background: var(--paper);
  }
  .sheet {
    position: relative;
    width: 1200px;
    height: 960px;
    font-family: "Arimo", sans-serif;
    font-weight: 400;
  }
  .card {
    position: absolute;
    top: 312px;
    width: 545px;
    height: 336px;
  }
  .card--front {
    left: 36px;
    background: var(--paper);
    border: 1px solid var(--edge);
  }
  .card--back {
    left: 619px;
    background: var(--navy);
    display: flex;
    align-items: center;
    justify-content: center;
  }

  /* Front: vertical firm name */
  .firm-vertical {
    position: absolute;
    left: 56px;
    top: 22px;
    height: 296px;
    display: flex;
    flex-direction: column;
    align-items: center;
    gap: 12px;
  }
  .firm-vertical__mark {
    width: 16px;
    height: 16px;
    background: var(--navy);
    flex: none;
  }
  .firm-vertical__name {
    writing-mode: vertical-rl;
    font-size: 21px;
    color: var(--navy);
    white-space: nowrap;
  }

  /* Front: holder */
  .holder {
    position: absolute;
    right: 46px;
    top: 52px;
    text-align: right;
    color: var(--ink);
  }
  .holder__name {
    font-size: 34px;
    line-height: 1.1;
  }
  .holder__title {
    font-size: 21px;
    letter-spacing: 1.6px;
    margin-top: 4px;
  }

  /* Front: contacts */
  .contacts {
    position: absolute;
    left: 140px;
    top: 204px;
    list-style: none;
    font-size: 20px;
    color: var(--ink);
  }
  .contacts__item {
    display: flex;
    align-items: center;
    gap: 9px;
    height: 30px;
  }
  .contacts__icon {
    width: 24px;
    height: 24px;
    flex: none;
  }

  /* Back: firm name */
  .firm-lockup {
    display: flex;
    align-items: center;
    gap: 14px;
    color: var(--paper);
  }
  .firm-lockup__mark {
    width: 24px;
    height: 24px;
    background: var(--paper);
    flex: none;
  }
  .firm-lockup__name {
    font-size: 34px;
    line-height: 1;
    white-space: nowrap;
  }
</style>
</head>
<body>
<main class="sheet">

  <section class="card card--front" aria-label="Card front">
    <div class="firm-vertical">
      <span class="firm-vertical__mark"></span>
      <span class="firm-vertical__name">Valdera Immigration Law</span>
    </div>

    <div class="holder">
      <p class="holder__name">Name</p>
      <p class="holder__title">Designation</p>
    </div>

    <ul class="contacts">
      <li class="contacts__item">
        <svg class="contacts__icon" viewBox="0 0 24 24" aria-hidden="true">
          <circle cx="12" cy="12" r="12" fill="#1c1c1c"/>
          <path d="M8.2 6.2l2 2.4-1.1 1.4c.8 1.7 2.1 3 3.9 3.9l1.4-1.1 2.4 2-1.3 1.9c-4.3-.6-8.5-4.8-9.1-9.1z" fill="#fff"/>
        </svg>
        <span>PH: 000</span>
      </li>
      <li class="contacts__item">
        <svg class="contacts__icon" viewBox="0 0 24 24" aria-hidden="true">
          <circle cx="12" cy="12" r="12" fill="#1c1c1c"/>
          <rect x="6" y="8" width="12" height="8.5" fill="#fff"/>
          <path d="M6 8l6 5 6-5" fill="none" stroke="#1c1c1c" stroke-width="1.2"/>
        </svg>
        <span>Email: @.com</span>
      </li>
      <li class="contacts__item">
        <svg class="contacts__icon" viewBox="0 0 24 24" aria-hidden="true">
          <circle cx="12" cy="12" r="12" fill="#1c1c1c"/>
          <g fill="none" stroke="#fff" stroke-width="1.2">
            <circle cx="12" cy="12" r="7"/>
            <ellipse cx="12" cy="12" rx="3" ry="7"/>
            <path d="M5 12h14M6 8.5h12M6 15.5h12"/>
          </g>
        </svg>
        <span>www.00000</span>
      </li>
    </ul>
  </section>

  <section class="card card--back" aria-label="Card back">
    <div class="firm-lockup">
      <span class="firm-lockup__mark"></span>
      <p class="firm-lockup__name">Valdera Immigration Law</p>
    </div>
  </section>

</main>
</body>
</html>
```